Coastal Bright Sweep Business Card

We are a cleaning and waste management company with the slogan "making waste to landfill a thing of the past". We would like a re-design of our current business card. On the front we want to continue to use our logo as the focus point. On the back, we want the whole thing re-done to be less busy. We want the staff member’s name, the job title, mobile number, email and website. We do not want the address on the card. We still want the green, black and blue colours used, but a new font for the information on the back. Please do not change the logo design at all. We are also thinking about using icons to replace the text ‘mobile, email, website’. The “events + commercial” banner needs to be incorporated somewhere and needs to read “events + commercial + waste”. Another important point for consideration is that we are very concerned about being environmentally sustainable and will be printing on recycled paper. All designs should be made to compliment this in regards to boldness and colouring. Please find attached our logo, our colour chart and an image of our current business card.

```html
<!DOCTYPE html>
<html lang="en">
<head>
<meta charset="utf-8">
<title>Coastal Bright Sweep – Business Card</title>
<link rel="stylesheet" href="https://fonts.googleapis.com/css2?family=Source+Serif+4:wght@400;600&family=Playfair+Display:wght@800&display=swap">
<style>
  :root {
    --navy: #1a4272;
    --green: #7dc142;
    --sky: #29abe2;
    --ink: #1d1d1f;
    --paper: #ffffff;
    --backdrop: #e6e7e9;
  }
  * { box-sizing: border-box; margin: 0; padding: 0; }
  html, body { width: 1200px; height: 1200px; overflow: hidden; }
  body {
    background: var(--backdrop);
    position: relative;
    font-family: "Source Serif 4", Georgia, serif;
  }
  .card {
    position: absolute;
    left: 222px;
    width: 756px;
    height: 456px;
    background: var(--paper);
    overflow: hidden;
  }
  .card--front { top: 126px; }
  .card--back { top: 645px; }

  .card__stripe {
    position: absolute; left: 0; right: 0;
    height: 6px; background: var(--green);
  }
  .card__band {
    position: absolute; left: 0; right: 0; bottom: 0;
    background: var(--navy);
  }
  .card--front .card__stripe { top: 406px; }
  .card--front .card__band { top: 413px; }
  .card--back .card__stripe { top: 410px; }
  .card--back .card__band { top: 417px; }

  .wordmark {
    position: absolute; left: 0; right: 0;
    text-align: center;
    font-family: "Source Serif 4", Georgia, serif;
    font-weight: 600;
    color: var(--navy);
    line-height: 1.05;
  }
  .card--front .wordmark { top: 150px; font-size: 46px; }
  .card--back .wordmark { top: 52px; font-size: 40px; }

  .front-web {
    position: absolute; top: 376px; left: 0; right: 0;
    display: flex; justify-content: center; align-items: center; gap: 10px;
    font-size: 17px; font-weight: 600; color: var(--navy);
    letter-spacing: 0.3px;
  }

  .staff { position: absolute; top: 210px; left: 0; width: 792px; text-align: center; }
  .staff__name {
    font-family: "Playfair Display", Georgia, serif;
    font-weight: 800; font-size: 30px; color: var(--navy);
    letter-spacing: -0.5px; line-height: 1.1;
  }
  .staff__role { font-size: 17px; color: var(--green); margin-top: 2px; }

  .contact { position: absolute; top: 277px; left: 37px; list-style: none; }
  .contact__item {
    display: flex; align-items: center; gap: 14px;
    height: 31px; font-size: 17px; color: var(--ink);
  }
  .contact__item svg { flex: none; }

  .divider {
    position: absolute; left: 396px; top: 275px;
    width: 1px; height: 100px; background: var(--sky);
  }

  .service-banner {
    position: absolute; left: 436px; top: 325px;
    width: 320px; height: 29px;
    background: var(--navy);
    clip-path: polygon(14px 0, 100% 0, 100% 100%, 0 100%);
    color: var(--paper);
    font-size: 16px;
    white-space: nowrap;
    display: flex; align-items: center; justify-content: center;
    padding-left: 12px;
  }
</style>
</head>
<body>

<section class="card card--front" aria-label="Card front">
  <p class="wordmark">Coastal<br>Bright<br>Sweep</p>
  <p class="front-web">
    <svg width="19" height="19" viewBox="0 0 20 20" aria-hidden="true">
      <rect width="20" height="20" rx="3" fill="var(--sky)"/>
      <circle cx="10" cy="10" r="6.5" fill="none" stroke="#fff" stroke-width="1.8"/>
      <path d="M3.5 10h13M10 3.5v13" stroke="#fff" stroke-width="1.4"/>
    </svg>
    coastalbrightsweep.com.au
  </p>
  <div class="card__stripe"></div>
  <div class="card__band"></div>
</section>

<section class="card card--back" aria-label="Card back">
  <p class="wordmark">Coastal<br>Bright<br>Sweep</p>

  <div class="staff">
    <p class="staff__name">Jamie Whitford</p>
    <p class="staff__role">Client Manager</p>
  </div>

  <ul class="contact">
    <li class="contact__item">
      <svg width="19" height="19" viewBox="0 0 20 20" aria-hidden="true">
        <rect width="20" height="20" rx="2" fill="var(--sky)"/>
        <path d="M8 4.5c-1.6.6-2.4 2-2.4 5.5s.8 4.9 2.4 5.5l1-2.5-1.3-.8c-.3-1.4-.3-3 0-4.4l1.3-.8z" fill="#fff"/>
      </svg>
      <span>&nbsp;0478215903</span>
    </li>
    <li class="contact__item">
      <svg width="19" height="19" viewBox="0 0 20 20" aria-hidden="true">
        <rect width="20" height="20" rx="2" fill="var(--sky)"/>
        <rect x="4" y="5.5" width="12" height="9" fill="none" stroke="#fff" stroke-width="1.4"/>
        <path d="M4 5.5l6 5 6-5" fill="none" stroke="#fff" stroke-width="1.4"/>
      </svg>
      <span>jwhitford@coastalbrightsweep.com.au</span>
    </li>
    <li class="contact__item">
      <svg width="19" height="19" viewBox="0 0 20 20" aria-hidden="true">
        <rect width="20" height="20" rx="3" fill="var(--sky)"/>
        <circle cx="10" cy="10" r="6.5" fill="none" stroke="#fff" stroke-width="1.8"/>
        <path d="M3.5 10h13M10 3.5v13" stroke="#fff" stroke-width="1.4"/>
      </svg>
      <span>coastalbrightsweep.com.au</span>
    </li>
  </ul>

  <div class="divider"></div>

  <p class="service-banner">Events + Commercial + Waste</p>

  <div class="card__stripe"></div>
  <div class="card__band"></div>
</section>

</body>
</html>
```